Business Card Design Project

I am looking for a minimal matte background/shiny (spot UV) ink monochromatic design with a splash of neon color.

the card should be 2 sided, logo only on one side - all info and possibly logo on the other.

My creative director described the colors he imagined for the design to be:
'it's a dark field, like charcoal or a really dark burgundy, or deep blue, shot through with a neon—but just a tiny bit of it. so a charcoal field with a laser-thin streak of electric lime, safety orange, or cobalt blue. really beautiful stuff.'

here are some samples of the types of cards I am trying to create:
http://www.pictavault.example/photos/dawnpress/6967376935/in/photostream -> Vandrelle Lustre

http://www.pictavault.example/photos/dawnpress/6497659409/in/photostream -> Standard Coated (14pt/matte) with SPOT UV

http://www.pictavault.example/photos/dawnpress/6497658995/in/photostream/ -> Heavy Corvane with Raised Ink

http://www.pictavault.example/photos/dawnpress/6275629165/in/photostream/ -> Standard Coated (14pt/matte) with SPOT UV

Here is my logo:
https://www.filecrate.example/s/sigym192mlh58ge/quillorb%20logotype%20final.ai

Here are the details for info:
Dorian Elwood Marsh
email - dorian@quillorb.example
mobile - 555 013 2867
web -
quillorb.example: inventive technology applications
quillorb-tv.example: innovative video advertising

please let me know if there is anything at all that you need.

Target Market(s)

mid to large agencies that require interactive design and entrepreneurial/startup individuals/companies that need application development.

Industry/Entity Type

Safety

Requirements
Must have
• logo only on one side

```html
<!DOCTYPE html>
<html lang="en">
<head>
<meta charset="utf-8">
<title>Quillorb Business Card</title>
<link href="https://fonts.googleapis.com/css2?family=PT+Sans:wght@400;700&display=swap" rel="stylesheet">
<style>
  :root {
    --backdrop: #3a3a3a;
    --card: #1c1c1d;
    --card-back: #151516;
    --ink-white: #f2f2f2;
    --ink-gloss: #4a4a4c;
    --lime: #7ac142;
    --muted: #cfcfcf;
  }
  * { box-sizing: border-box; margin: 0; padding: 0; }
  html, body { width: 1200px; height: 716px; overflow: hidden; }
  body {
    background: var(--backdrop);
    font-family: "PT Sans", sans-serif;
    position: relative;
  }
  .card {
    position: absolute;
    top: 215px;
    width: 500px;
    height: 286px;
    border-radius: 4px;
    box-shadow: 0 10px 30px rgba(0,0,0,.45);
    overflow: hidden;
  }
  .card--front { left: 70px; background: var(--card); }
  .card--back { left: 630px; background: var(--card-back); }

  .wordmark {
    position: absolute;
    display: flex;
    align-items: center;
    gap: 10px;
    font-weight: 700;
    text-transform: uppercase;
  }
  .wordmark__dot { border-radius: 50%; background: var(--lime); }
  .card--front .wordmark { left: 34px; top: 58px; font-size: 24px; letter-spacing: 6px; color: var(--ink-white); }
  .card--front .wordmark__dot { width: 10px; height: 10px; }
  .card--back .wordmark { left: 50%; top: 50%; transform: translate(-50%, -50%); font-size: 34px; letter-spacing: 10px; color: var(--ink-gloss); }
  .card--back .wordmark__dot { width: 14px; height: 14px; }

  .uv-pattern {
    position: absolute;
    left: 270px; top: 18px;
    width: 190px; height: 220px;
    border-radius: 30px;
    background: radial-gradient(ellipse at 50% 45%, #3b3b3d 0%, #2a2a2c 55%, rgba(28,28,29,0) 80%);
  }

  .holder { position: absolute; left: 34px; top: 132px; }
  .holder__marker {
    position: absolute; left: -34px; top: 3px;
    width: 0; height: 0;
    border-top: 7px solid transparent;
    border-bottom: 7px solid transparent;
    border-left: 9px solid var(--lime);
  }
  .holder__name { color: var(--ink-white); font-size: 16px; line-height: 19px; }
  .holder__title { color: var(--lime); font-size: 12px; line-height: 14px; }

  .contact { position: absolute; left: 34px; top: 198px; list-style: none; }
  .contact__item {
    display: flex; align-items: center; gap: 7px;
    height: 15px;
    color: var(--ink-white); font-size: 12px;
  }
  .contact__item svg { width: 11px; height: 11px; flex: none; }
  .contact__tagline { color: var(--lime); font-size: 10px; margin-left: 14px; }
</style>
</head>
<body>

  <section class="card card--front" aria-label="Card front with contact details">
    <div class="wordmark"><span>Quillorb</span><span class="wordmark__dot"></span></div>

    <div class="uv-pattern" role="img" aria-label="Glossy spot UV hexagon cluster pattern"></div>

    <div class="holder">
      <span class="holder__marker"></span>
      <p class="holder__name">Dorian Elwood Marsh</p>
      <p class="holder__title">Founder &amp; CEO</p>
    </div>

    <ul class="contact">
      <li class="contact__item">
        <svg viewBox="0 0 12 12"><rect x="0.5" y="2" width="11" height="8" fill="none" stroke="#7ac142" stroke-width="1.2"/><path d="M1 2.5 6 7 11 2.5" fill="none" stroke="#7ac142" stroke-width="1.2"/></svg>
        dorian@quillorb.example
      </li>
      <li class="contact__item">
        <svg viewBox="0 0 12 12"><rect x="3" y="0.5" width="6" height="11" rx="1" fill="none" stroke="#7ac142" stroke-width="1.2"/><circle cx="6" cy="9.5" r="0.8" fill="#7ac142"/></svg>
        555 013 2867
      </li>
      <li class="contact__item">
        <svg viewBox="0 0 12 12"><circle cx="6" cy="6" r="5.2" fill="none" stroke="#7ac142" stroke-width="1.2"/><path d="M1 6h10M6 1c-2.5 3-2.5 7 0 10M6 1c2.5 3 2.5 7 0 10" fill="none" stroke="#7ac142" stroke-width="1"/></svg>
        quillorb.example
        <span class="contact__tagline">inventive technology applications</span>
      </li>
      <li class="contact__item">
        <svg viewBox="0 0 12 12"><circle cx="6" cy="6" r="5.2" fill="none" stroke="#7ac142" stroke-width="1.2"/><path d="M1 6h10M6 1c-2.5 3-2.5 7 0 10M6 1c2.5 3 2.5 7 0 10" fill="none" stroke="#7ac142" stroke-width="1"/></svg>
        quillorb-tv.example
        <span class="contact__tagline">innovative video advertising</span>
      </li>
    </ul>
  </section>

  <section class="card card--back" aria-label="Card back with name mark">
    <div class="wordmark"><span>Quillorb</span><span class="wordmark__dot"></span></div>
  </section>

</body>
</html>
```